Dog Coat Drive for San Francisco Homeless Pets

- one page, full color, flyer to advertise a winter dog coat drive.- requesting use of an image of pit bull type or chihuahua type dog in a coat - 2 size versions - 8.5 inch by 11 inch to be printed and a square design to be posted on FB, Instagram and websites

Font styles to use
Serif
Sans Serif

Colors

Designer to choose colors to be used in the design.

```html
<!DOCTYPE html>
<html lang="en">
<head>
<meta charset="utf-8">
<title>Dog Coat Drive</title>
<link rel="stylesheet" href="https://fonts.googleapis.com/css2?family=Archivo+Black&family=Outfit:wght@400;600;700&display=swap">
<style>
  :root {
    --navy: #1a5e96;
    --deep: #155384;
    --sky: #79c8ef;
    --frost: #dde9f2;
    --white: #ffffff;
    --ink: #1f1f22;
  }
  * { margin: 0; padding: 0; box-sizing: border-box; }
  html, body { width: 900px; height: 1200px; overflow: hidden; background: var(--navy); }
  .flyer { position: relative; width: 900px; height: 1200px; font-family: "Outfit", sans-serif; color: var(--ink); overflow: hidden; }
  .backdrop { position: absolute; inset: 0; }
  .brand {
    position: absolute; left: 28px; top: 65px; width: 274px; height: 91px;
    background: var(--white); display: flex; align-items: center; gap: 12px; padding-left: 20px;
  }
  .brand-dot { width: 30px; height: 30px; border-radius: 50%; background: var(--navy); flex: none; }
  .brand-name { font-weight: 700; font-size: 25px; color: var(--navy); line-height: 1; white-space: nowrap; }
  .brand-tag { display: block; font-size: 12.5px; font-weight: 600; color: var(--ink); margin-top: 4px; text-align: right; }
  .headline {
    position: absolute; left: 46px; top: 392px;
    font-family: "Archivo Black", sans-serif; font-size: 88px; line-height: 84px;
    color: var(--navy); letter-spacing: -2px; text-transform: uppercase; white-space: nowrap;
    text-shadow:
      3px 0 0 var(--white), -3px 0 0 var(--white), 0 3px 0 var(--white), 0 -3px 0 var(--white),
      3px 3px 0 var(--white), -3px -3px 0 var(--white), 3px -3px 0 var(--white), -3px 3px 0 var(--white),
      5px 0 0 var(--navy), -5px 0 0 var(--navy), 0 5px 0 var(--navy), 0 -5px 0 var(--navy),
      5px 5px 0 var(--navy), -5px -5px 0 var(--navy), 5px -5px 0 var(--navy), -5px 5px 0 var(--navy);
  }
  .appeal { position: absolute; left: 51px; top: 664px; width: 462px; font-size: 20px; line-height: 25px; }
  .coat-samples { position: absolute; left: 62px; top: 772px; display: flex; gap: 10px; }
  .coat-samples div { width: 88px; height: 62px; border-radius: 12px; }
  .coat-red { background: linear-gradient(135deg, #d8272b, #9e1b1e); }
  .coat-plaid { background: linear-gradient(135deg, #c9b79c, #8a6f55); }
  .coat-navy { background: linear-gradient(135deg, #2b3446, #161b26); }
  .drive-card {
    position: absolute; left: 623px; top: 768px; width: 249px; height: 230px;
    background: var(--white); padding: 6px 12px 0 13px;
  }
  .drive-word { font-family: "Archivo Black", sans-serif; font-size: 88px; line-height: 82px; color: var(--navy); letter-spacing: -2px; }
  .drive-title { font-weight: 700; font-size: 35px; line-height: 36px; color: var(--ink); letter-spacing: 0.5px; white-space: nowrap; }
  .drive-for { font-size: 18px; line-height: 22px; padding-bottom: 6px; border-bottom: 2px solid var(--navy); }
  .drive-dates { font-weight: 700; font-size: 25px; line-height: 29px; margin-top: 6px; white-space: nowrap; }
  .partners {
    position: absolute; left: 28px; top: 1030px; width: 844px; height: 142px;
    background: var(--white); border-radius: 8px; box-shadow: 0 0 0 2px var(--sky);
    display: flex; padding: 16px 0 12px;
  }
  .partners-title {
    position: absolute; top: -10px; left: 50%; transform: translateX(-50%);
    background: var(--navy); color: var(--white); font-size: 15px; padding: 0 8px; white-space: nowrap;
  }
  .partner { padding: 0 10px; border-left: 1px solid var(--navy); white-space: nowrap; }
  .partner:first-child { border-left: none; }
  .partner-a { flex: 0 0 118px; }
  .partner-b { flex: 0 0 170px; }
  .partner-c { flex: 0 0 160px; }
  .partner-d { flex: 0 0 200px; }
  .partner-e { flex: 1 1 auto; }
  .partner-badge { height: 52px; display: flex; align-items: center; margin-bottom: 10px; }
  .badge-circle { width: 50px; height: 50px; border-radius: 50%; background: var(--navy); }
  .badge-square { width: 46px; height: 46px; background: var(--sky); }
  .badge-bar { width: 128px; height: 18px; background: var(--deep); }
  .badge-warm { width: 48px; height: 48px; border-radius: 50%; background: #1c1c1c; }
  .badge-leaf { width: 46px; height: 46px; background: #8cbf5a; }
  .partner-name { font-weight: 700; font-size: 12.5px; line-height: 15px; }
  .partner-line { font-size: 11.5px; line-height: 14px; }
  .partner-phone { font-weight: 700; font-size: 12.5px; line-height: 15px; }
</style>
</head>
<body>
<main class="flyer">
  <svg class="backdrop" width="900" height="1200" viewBox="0 0 900 1200">
    <defs>
      <linearGradient id="snowfield" x1="0" y1="0" x2="1" y2="1">
        <stop offset="0" stop-color="#c8dcea"/>
        <stop offset="0.5" stop-color="#e6eef5"/>
        <stop offset="1" stop-color="#f4f7fa"/>
      </linearGradient>
      <radialGradient id="dogglow" cx="0.63" cy="0.42" r="0.3">
        <stop offset="0" stop-color="#e3c6ad"/>
        <stop offset="1" stop-color="#e3c6ad" stop-opacity="0"/>
      </radialGradient>
    </defs>
    <rect width="900" height="1200" fill="var(--navy)"/>
    <polygon points="0,240 75,316 499,94 900,158 900,883 779,761 344,985 0,921" fill="var(--sky)"/>
    <g role="img" aria-label="Photo of a small long-haired chihuahua running through falling snow">
      <polygon points="0,318 75,366 499,131 900,200 900,841 779,713 344,937 0,889" fill="url(#snowfield)"/>
      <polygon points="0,318 75,366 499,131 900,200 900,841 779,713 344,937 0,889" fill="url(#dogglow)"/>
    </g>
  </svg>

  <div class="brand">
    <span class="brand-dot"></span>
    <div class="brand-name">WarmTummy Van<span class="brand-tag">Mobile Pet Care Team</span></div>
  </div>

  <h1 class="headline">Baby,<br>It's Cold<br>Outside!</h1>

  <p class="appeal">Please donate new &amp; gently used dog coats, sweaters and jackets for Shelter Hub dogs whose owners are working to prevent and end their homelessness</p>

  <div class="coat-samples">
    <div class="coat-red" role="img" aria-label="Red padded dog jacket"></div>
    <div class="coat-plaid" role="img" aria-label="Plaid dog coat on a white mannequin"></div>
    <div class="coat-navy" role="img" aria-label="Navy dog coat on a white mannequin"></div>
  </div>

  <section class="drive-card">
    <div class="drive-word">DOG</div>
    <div class="drive-title">COAT DRIVE</div>
    <div class="drive-for">for Bay Shelter Hubs</div>
    <div class="drive-dates">from December ‘<br>through February</div>
  </section>

  <section class="partners">
    <span class="partners-title">COAT DROP PARTNERS AND LOCATIONS</span>
    <div class="partner partner-a">
      <div class="partner-badge"><span class="badge-square"></span></div>
      <div class="partner-name">City Pet Shelter</div>
      <div class="partner-line">410 Harbor Street</div>
      <div class="partner-phone">415-555-0142</div>
    </div>
    <div class="partner partner-b">
      <div class="partner-badge"><span class="badge-circle"></span></div>
      <div class="partner-name">The Kennel Corner</div>
      <div class="partner-line">88 Maple Street</div>
      <div class="partner-phone">415-555-0178</div>
    </div>
    <div class="partner partner-c">
      <div class="partner-badge"><span class="badge-warm"></span></div>
      <div class="partner-name">Hillside Pet Co.</div>
      <div class="partner-line">1320 Oak Street</div>
      <div class="partner-phone">415-555-0193</div>
    </div>
    <div class="partner partner-d">
      <div class="partner-badge"><span class="badge-leaf"></span></div>
      <div class="partner-name">Happy Tails Pet Services</div>
      <div class="partner-line">25 Seaview Drive, Coastview</div>
      <div class="partner-phone">650-555-0116</div>
    </div>
    <div class="partner partner-e">
      <div class="partner-badge"><span class="badge-bar"></span></div>
      <div class="partner-name">The Bark Center</div>
      <div class="partner-line">702 Shore Avenue, Coastview</div>
      <div class="partner-phone">650-555-0127</div>
    </div>
  </section>
</main>
</body>
</html>
```